Cover Page for Financial Statements

We need a cover page designed for our Financial Statements. It will need to include our business logo and the Chartered accountant logo.
We have included our current title page ( image titled full.png ) to show all the information that is needed to be included such as the title 'Financial Statements' and 'The year ended March 2023'. We would like to see designs that reflect our logo but also adds some interest with objects / deisngs that fill up more of the page.

Industry/Entity Type

Accounting

Font styles to use
Serif
Sans Serif

Colors

Designer to choose only greyscale colors for use in the design.

Requirements
Must have
• - A4 document size, our logo, Chartered Accountant Logo
Should not have
• Bright Colors

```html
<!DOCTYPE html>
<html lang="en">
<head>
<meta charset="utf-8">
<title>Financial Statements – Year Ended March 2023</title>
<link rel="stylesheet" href="https://fonts.googleapis.com/css2?family=Jost:wght@400;500&display=swap">
<style>
  :root {
    --page: #ffffff;
    --ink: #111111;
    --title: #2a2a2a;
    --accent: #7a7a7a;
    --accent-dark: #4a4a4a;
    --accent-darker: #3a3a3a;
    --shade: #5e5e5e;
    --shade-deep: #3f3f3f;
    --mist: #d6d7da;
    --mist-light: #f1f1f3;
    --badge: #dcdde0;
  }
  html, body {
    margin: 0;
    padding: 0;
    width: 920px;
    height: 1200px;
    overflow: hidden;
    background: var(--page);
  }
  .cover {
    display: block;
    width: 920px;
    height: 1200px;
    font-family: "Jost", "Helvetica Neue", Arial, sans-serif;
  }
  .brand-name { font-size: 27px; font-weight: 400; fill: var(--ink); letter-spacing: 1.5px; }
  .title-small { font-size: 41px; font-weight: 400; fill: var(--title); }
  .title-large { font-size: 77px; font-weight: 500; fill: var(--title); }
  .period-label { font-size: 44px; font-weight: 400; fill: var(--accent); }
  .period-date { font-size: 44px; font-weight: 400; fill: var(--title); }
</style>
</head>
<body>
<svg class="cover" viewBox="0 0 920 1200" xmlns="http://www.w3.org/2000/svg">
  <defs>
    <linearGradient id="mist-fade" x1="0" y1="0" x2="1" y2="0">
      <stop offset="0" stop-color="#ffffff"/>
      <stop offset="0.5" stop-color="var(--mist-light)"/>
      <stop offset="1" stop-color="var(--mist)"/>
    </linearGradient>
    <linearGradient id="top-wave" x1="0" y1="0" x2="1" y2="0">
      <stop offset="0" stop-color="var(--accent-dark)"/>
      <stop offset="1" stop-color="var(--accent-darker)"/>
    </linearGradient>
    <linearGradient id="bottom-wave" x1="0" y1="0" x2="1" y2="0">
      <stop offset="0" stop-color="var(--shade-deep)"/>
      <stop offset="1" stop-color="var(--shade)"/>
    </linearGradient>
    <linearGradient id="mist-low" x1="0" y1="0" x2="1" y2="0">
      <stop offset="0" stop-color="#e6e7ea"/>
      <stop offset="1" stop-color="#ffffff"/>
    </linearGradient>
    <linearGradient id="mesh-tone" x1="0" y1="1" x2="1" y2="0">
      <stop offset="0" stop-color="#f4f4f5" stop-opacity="0.3"/>
      <stop offset="1" stop-color="#cfd0d3" stop-opacity="0.7"/>
    </linearGradient>
  </defs>

  <!-- flowing mesh area -->
  <path class="mesh-band" role="img" aria-label="Flowing fine line mesh pattern"
        fill="url(#mesh-tone)"
        d="M235,1130 C220,960 300,760 430,560 C520,430 620,300 700,240 L760,260 C700,360 610,470 520,550 C420,640 330,760 270,900 C245,960 240,1060 235,1130 Z"/>

  <!-- top-right shapes -->
  <path class="mist-top" fill="url(#mist-fade)"
        d="M410,0 C470,18 505,40 525,70 C545,100 575,100 610,95 C660,90 700,140 705,185 C710,240 780,270 860,280 C890,282 910,278 920,277 L920,0 Z"/>
  <path class="top-wave" fill="url(#top-wave)"
        d="M498,0 C540,30 585,45 625,65 C660,85 675,125 692,150 C705,170 678,200 700,220 C740,245 840,248 920,233 L920,0 Z"/>
  <ellipse class="top-glow" cx="690" cy="105" rx="55" ry="40" fill="#8a8a8a" opacity="0.6"/>

  <!-- brand -->
  <g class="brand">
    <rect x="62" y="88" width="16" height="16" fill="var(--ink)"/>
    <text class="brand-name" x="90" y="106">LEDGERWAY FINANCIAL</text>
  </g>

  <!-- title block -->
  <g class="title-block">
    <rect class="accent-bar" x="591" y="476" width="84" height="14" fill="var(--accent)"/>
    <path class="title-frame" fill="none" stroke="var(--title)" stroke-width="10"
          d="M356,706 L250,706 L250,519 L669,519 L669,582"/>
    <text class="title-small" x="284" y="590">FINANCIAL</text>
    <text class="title-large" x="282" y="655" textLength="398" lengthAdjust="spacingAndGlyphs">STATEMENTS</text>
    <text class="period-label" x="680" y="723" text-anchor="end" textLength="309" lengthAdjust="spacingAndGlyphs">THE YEAR ENDED</text>
    <text class="period-date" x="680" y="766" text-anchor="end" textLength="239" lengthAdjust="spacingAndGlyphs">MARCH 2023</text>
  </g>

  <!-- bottom-left shapes -->
  <path class="mist-bottom" fill="url(#mist-low)"
        d="M390,1090 C440,1062 505,1060 535,1085 C565,1112 575,1150 600,1185 L612,1200 L450,1200 Z"/>
  <path class="bottom-wave" fill="url(#bottom-wave)"
        d="M0,982 C90,945 230,950 330,1020 C400,1070 410,1120 430,1155 C450,1185 480,1190 505,1200 L0,1200 Z"/>
  <path class="bottom-shade" fill="var(--shade-deep)" opacity="0.55"
        d="M0,996 C60,982 150,978 205,988 C240,998 232,1040 215,1072 C198,1110 225,1140 268,1130 C315,1118 350,1095 390,1080 C420,1120 440,1170 505,1200 L0,1200 Z"/>

  <!-- accreditation badge -->
  <circle class="accreditation-badge" cx="765" cy="1098" r="34" fill="var(--badge)"/>
</svg>
</body>
</html>
```